Exterior cleaning company requires a eye catching a5 leaflet

we need some updated leaflet designs, a5 folded, we are targeting all exterior cleaning contracts, including roof cleaning & treatment, render cleaning & Treatment, driveways, block paving cleaning using the latest in low pressure cleaning technologies along side high pressure jetwashing. gutter clearance and flushing, water fed telescopic pole window cleaning of difficult to reach windows and high buildings. our website : www.tkbellowsec.co.uk facebook page: https://www.facebook.com/tkbellowsexteriorcareltd Instagram: https://www.instagram.com/tkbellowsec/ a quick google search of roof cleaning, soft washing etc will provide results of what we are doing

Target Market(s)

home owners, commercial clients

Font styles to use
Serif
Sans Serif

Requirements
Must have
• A5 Landscape folded leaflet, front page with company information and bullet points of main works : window & conservatory cleaning, roof cleaning & treatment, Render cleaning & treatment, pressure washing, soft washing, gutter clearing, pressure washing of patios, driveways, gutters, fascias (more info can be provided on techniques etc if required)

```html
<!DOCTYPE html>
<html lang="en">
<head>
<meta charset="utf-8">
<title>T.K Bellows Window Cleaning Ltd – Leaflet Spread</title>
<link rel="stylesheet" href="https://fonts.googleapis.com/css2?family=Archivo+Black&family=Source+Sans+3:wght@400;600;700&display=swap">
<style>
  :root {
    --ink: #0d0d0d;
    --paper: #ffffff;
    --orange: #ee9a1c;
    --orange-deep: #d9820f;
    --yellow: #f7b52b;
    --grey-text: #1c1c1c;
    --sidebar-text: #e8e8e8;
    --stage: #e8e8e8;
  }
  * { box-sizing: border-box; margin: 0; padding: 0; }
  html, body { width: 900px; height: 1200px; overflow: hidden; }
  body { background: var(--stage); position: relative; font-family: "Source Sans 3", Arial, sans-serif; color: var(--grey-text); }

  .spread { position: absolute; left: 20px; top: 298px; width: 860px; height: 604px; display: flex; }
  .page { position: relative; width: 430px; height: 604px; overflow: hidden; }

  /* ---------- inside page ---------- */
  .page--inside { background: var(--paper); }
  .experience-bar { position: absolute; left: 300px; top: 62px; width: 130px; height: 20px; background: var(--yellow); }
  .experience-heading {
    position: absolute; left: 74px; top: 56px; width: 266px; height: 32px;
    background: var(--paper); border: 2px solid var(--yellow);
    font-family: "Source Sans 3", Arial, sans-serif; font-weight: 700; font-size: 17px;
    line-height: 28px; padding-left: 10px; color: var(--ink); letter-spacing: .2px;
  }
  .intro { position: absolute; left: 19px; top: 124px; width: 404px; font-size: 11.6px; line-height: 15px; text-align: justify; }

  .contact-panel { position: absolute; left: 0; top: 198px; width: 151px; height: 406px; background: linear-gradient(180deg, #151515 0%, #0b0b0b 100%); color: var(--sidebar-text); }
  .contact-panel .pin { position: absolute; left: 37px; top: 26px; width: 76px; height: 80px; }
  .contact-panel .brand-name { position: absolute; left: 22px; top: 152px; font-family: "Source Sans 3", Arial, sans-serif; font-weight: 700; font-size: 15px; color: var(--yellow); letter-spacing: .3px; }
  .contact-panel .brand-sub { position: absolute; left: 22px; top: 170px; font-weight: 700; font-size: 10px; color: var(--sidebar-text); }
  .contact-panel .rule { position: absolute; left: 22px; width: 90px; height: 1px; background: var(--yellow); }
  .contact-panel .address { position: absolute; left: 28px; top: 228px; font-size: 11.5px; line-height: 15px; font-style: normal; }
  .contact-panel .phone { position: absolute; left: 28px; top: 332px; font-size: 11.5px; }

  .body-copy { position: absolute; left: 186px; top: 190px; width: 236px; font-size: 11.6px; line-height: 14.4px; text-align: justify; }
  .body-copy p + p { margin-top: 16px; }

  .band { position: absolute; top: 574px; height: 30px; background: linear-gradient(180deg, var(--yellow) 0%, var(--orange) 55%, var(--orange-deep) 100%); }
  .page--inside .band { left: 270px; width: 160px; }

  /* ---------- cover page ---------- */
  .page--cover { background: linear-gradient(90deg, #ffffff 0%, #ffffff 70%, #e2e2e2 100%); }
  .cover-lower { position: absolute; left: 0; top: 400px; width: 430px; height: 204px; background: var(--ink); }
  .wordmark { position: absolute; left: 0; top: 22px; width: 430px; text-align: center; font-family: "Archivo Black", Arial, sans-serif; font-size: 40px; line-height: 48px; color: var(--ink); letter-spacing: .5px; }
  .wordmark-sub { position: absolute; left: 0; top: 70px; width: 430px; text-align: center; font-family: "Source Sans 3", Arial, sans-serif; font-weight: 700; font-size: 14px; color: var(--ink); }
  .sectors { position: absolute; left: 74px; top: 95px; width: 282px; height: 20px; border: 1px solid var(--yellow); border-top: none; text-align: center; font-size: 10.5px; line-height: 18px; color: var(--ink); }
  .hero-photo {
    position: absolute; left: 22px; top: 134px; width: 376px; height: 290px;
    background:
      linear-gradient(180deg, rgba(13,13,13,0) 62%, rgba(13,13,13,1) 100%),
      linear-gradient(180deg, #d9d6d2 0%, #8a4a36 28%, #7a3b2a 55%, #5d4a3e 80%, #3a3632 100%);
  }
  .services { position: absolute; top: 458px; list-style: none; color: #f2f2f2; font-size: 11px; line-height: 19px; }
  .services--a { left: 46px; }
  .services--b { left: 234px; }
  .services li { position: relative; padding-left: 16px; }
  .services li::before { content: ""; position: absolute; left: 0; top: 5px; width: 9px; height: 9px; border: 2px solid var(--orange); border-radius: 50%; }
  .page--cover .band { left: 0; width: 430px; }
  .website { position: absolute; left: 0; top: 574px; width: 430px; text-align: center; font-size: 11px; line-height: 30px; letter-spacing: 2.2px; color: var(--ink); font-weight: 600; }
</style>
</head>
<body>
  <main class="spread">
    <section class="page page--inside">
      <div class="experience-bar"></div>
      <h2 class="experience-heading">OVER 10 YEARS EXPERIENCE</h2>
      <p class="intro">T.K Bellows Window Cleaning is Southport’s most reliable, professional cleaning company who have been providing cleaning services across the North West for 10 years!</p>

      <aside class="contact-panel">
        <svg class="pin" viewBox="0 0 76 80" aria-hidden="true">
          <ellipse cx="38" cy="64" rx="30" ry="10" fill="none" stroke="#6a6a6a" stroke-width="3"/>
          <path d="M38 4c-13 0-23 10-23 23 0 17 23 40 23 40s23-23 23-40C61 14 51 4 38 4z" fill="#6a6a6a"/>
          <circle cx="38" cy="27" r="9" fill="#151515"/>
        </svg>
        <div class="brand-name">T.K BELLOWS</div>
        <div class="brand-sub">Window Cleaning Ltd</div>
        <div class="rule" style="top:190px"></div>
        <address class="address">14 Larkmoor Rd<br>(8,103.68 km)<br>PR9 4ZX Southport</address>
        <div class="rule" style="top:302px"></div>
        <div class="phone">+44 1700 900412</div>
      </aside>

      <div class="body-copy">
        <p>At T.K Bellows, our mission is to lead our sector in providing all of our customers with an outstanding cleaning service that keeps ourselves one step ahead of our competition. All of our staff are uniformed, polite, courteous and always happy to help. We aim to build long lasting relationships with our customers, and offer a 5* customer service team to help resolve any issues that may arise.</p>
        <p>Whether it’s to improve overall results or safety, we are always on the lookout for the latest equipment that gives the best finish possible. At T.K Bellows our staff use the reach &amp; wash system, otherwise known as the ‘water fed pole’. A technique which compared to traditional window cleaning, reaches your windows and frames safely from the ground, even</p>
      </div>
      <div class="band"></div>
    </section>

    <section class="page page--cover">
      <div class="cover-lower"></div>
      <h1 class="wordmark">T.K BELLOWS</h1>
      <div class="wordmark-sub">Window Cleaning Ltd</div>
      <div class="sectors">Commercial • Domestic • Industrial • Retail Cleaning</div>
      <div class="hero-photo" role="img" aria-label="Photograph of a large red-brick period house with bay windows and stone steps, a cleaner washing the windows with a water fed pole"></div>
      <ul class="services services--a">
        <li>pressure washing, soft washing,</li>
        <li>gutter clearing,</li>
        <li>pressure washing of patios</li>
        <li>driveways</li>
        <li>fascias</li>
      </ul>
      <ul class="services services--b">
        <li>window &amp; conservatory cleaning</li>
        <li>roof cleaning &amp; treatment</li>
        <li>Render cleaning &amp; treatment</li>
        <li>gutters</li>
      </ul>
      <div class="band"></div>
      <div class="website">www.tkbellowsec.co.uk</div>
    </section>
  </main>
</body>
</html>
```